Brexalinth Web Design

We would like to have our website designed and coded. It will be a display only website - no input or output functionality. It's a fairly simple structure with not many pages, but we would like some professional design and creative elements added in to make the site attractive and sharp. I have attached a presentation with the page and content layout. Where images are included in the presentation, those are concepts that you can reorganize or layout in any way that you think looks best. Same with the wheel of services on the incubator page, and the bullet points listed on the accelerator page.

```html
<!DOCTYPE html>
<html lang="en">
<head>
<meta charset="utf-8">
<title>Brexalinth</title>
<link href="https://fonts.googleapis.com/css2?family=Lato:wght@400;700;900&display=swap" rel="stylesheet">
<style>
:root{
  --navy:#0f2a4a;
  --navy-deep:#0a1e36;
  --ink:#1d1d1d;
  --muted:#555b63;
  --grey-band:#e4e4e4;
  --footer:#0b0b0c;
  --white:#ffffff;
}
*{box-sizing:border-box;margin:0;padding:0}
html,body{width:1200px;height:3252px;overflow:hidden}
body{font-family:"Lato",Arial,sans-serif;color:var(--ink);background:var(--white);position:relative}
.abs{position:absolute}

/* header */
.site-header{position:absolute;top:0;left:0;width:1200px;height:52px;background:var(--white);z-index:5;display:flex;align-items:center;justify-content:space-between;padding:0 110px 0 112px}
.brand{font-weight:900;font-size:26px;letter-spacing:1px;color:var(--navy)}
.main-nav{display:flex;gap:30px;font-size:14px;color:#333}

/* hero */
.hero{position:absolute;top:52px;left:0;width:1200px;height:600px;overflow:hidden}
.hero-photo{position:absolute;inset:0;background:linear-gradient(180deg,#3a3d42 0%,#5c6066 45%,#2e3136 100%)}
.hero-title{left:112px;top:280px;color:var(--white);font-size:38px;font-weight:700}
.hero-text{left:112px;top:340px;width:360px;color:#e8e8e8;font-size:15px;line-height:1.55}
.btn{display:inline-flex;align-items:center;gap:8px;background:var(--navy);color:var(--white);font-size:14px;font-weight:700;padding:11px 22px;border-radius:22px}
.btn .dot{width:14px;height:14px;border-radius:50%;background:var(--white);display:inline-block;position:relative}
.btn .dot::after{content:"";position:absolute;left:4px;top:4px;border-left:6px solid var(--navy);border-top:3px solid transparent;border-bottom:3px solid transparent}
.hero-btn{left:112px;top:418px}
.slider-dots{right:52px;top:330px;display:flex;flex-direction:column;gap:22px}
.slider-dots span{width:12px;height:12px;border-radius:50%;border:2px solid var(--white)}
.slider-dots span.on{background:var(--white)}
.hero-wave{position:absolute;left:0;top:480px}

/* about */
.about-photo{left:150px;top:800px;width:420px;height:420px;border-radius:50%;background:radial-gradient(circle at 45% 40%,#cfcfcf,#7d7f82 70%,#55585c);box-shadow:12px 16px 0 -2px var(--navy)}
.section-title{font-size:32px;font-weight:700;color:var(--ink)}
.about-title{left:640px;top:860px}
.about-text{left:640px;top:920px;width:440px;font-size:15px;line-height:1.75;color:var(--muted)}
.about-btn{left:640px;top:1150px}

/* services */
.services{left:0;top:1340px;width:1200px;height:570px;background:var(--grey-band)}
.services-title{left:0;width:1200px;top:80px;text-align:center}
.service-row{left:80px;top:148px;width:1040px;display:grid;grid-template-columns:repeat(4,1fr)}
.service{display:flex;flex-direction:column;align-items:center;text-align:center}
.service-icon{width:206px;height:206px;border-radius:50%;background:var(--white);border:10px solid var(--white);box-shadow:8px 6px 0 0 var(--navy);display:flex;align-items:center;justify-content:center}
.service-icon i{width:110px;height:110px;border-radius:50%;background:#d6dde6;display:block}
.service h3{margin-top:24px;font-size:19px;font-weight:700;line-height:1.3;color:var(--ink)}
.service p{margin-top:12px;font-size:15px;line-height:1.6;color:var(--muted);width:200px}
.arrow{top:240px;font-size:22px;color:#333}

/* located */
.located-title{left:112px;top:2020px;font-size:40px;line-height:1.25}
.map{left:112px;top:2140px;width:392px;height:382px;background:linear-gradient(135deg,#e9ecef,#bfc6cd)}
.timeline{left:552px;top:2030px;width:610px;border-left:2px solid #c8c8c8;list-style:none}
.timeline li{position:relative;padding:0 0 14px 30px;font-size:15px;line-height:1.6;color:var(--muted)}
.timeline li::before{content:"";position:absolute;left:-7px;top:6px;width:12px;height:12px;border-radius:50%;background:var(--navy)}

/* footer */
.footer-wave{position:absolute;left:0;top:2590px}
.footer{left:0;top:2760px;width:1200px;height:492px;background:var(--footer);color:#ddd}
.footer-brand{left:112px;top:50px;font-size:30px;color:var(--white)}
.footer-col{top:140px;font-size:14px;line-height:2}
.footer-col h4{font-size:16px;color:var(--white);font-weight:700;margin-bottom:8px}
.newsletter-title{left:592px;top:52px;font-size:28px;color:var(--white);font-weight:700}
.news-input{left:592px;top:118px;width:300px;border-bottom:1px solid #777;padding-bottom:10px;font-size:14px;color:#999}
.news-btn{left:940px;top:108px;background:var(--navy);color:var(--white);font-weight:700;font-size:14px;padding:11px 26px;border-radius:20px}
.contact-line{left:592px;top:190px;display:flex;gap:28px;font-size:14px;align-items:center}
.socials{display:flex;gap:12px}
.socials span{width:12px;height:12px;border-radius:50%;background:#cfcfcf}
.faint-name{left:592px;top:260px;font-size:86px;font-weight:900;color:#1a1a1c;letter-spacing:4px}
.footer-rule{left:112px;top:400px;width:976px;height:1px;background:#333}
.copyright{left:0;width:1200px;top:425px;text-align:center;font-size:14px;color:#bbb}
</style>
</head>
<body>

<header class="site-header">
  <div class="brand">BREXALINTH</div>
  <nav class="main-nav"><span>Home</span><span>Incubator</span><span>Accelerator</span><span>UAE Distribution</span><span>References</span><span>Contact Us</span></nav>
</header>

<section class="hero">
  <div class="hero-photo" role="img" aria-label="Black and white city skyline photo"></div>
  <h1 class="abs hero-title">Welcome To Brexalinth</h1>
  <p class="abs hero-text">Brexalinth is a global incubator for start-up and early-stage medical device companies and ventures.</p>
  <a class="abs btn hero-btn">Learn More <span class="dot"></span></a>
  <div class="abs slider-dots"><span class="on"></span><span></span><span></span><span></span></div>
  <svg class="hero-wave" width="1200" height="120" viewBox="0 0 1200 120">
    <path d="M0 40 C300 110 800 110 1200 20 L1200 120 L0 120Z" fill="var(--navy)"/>
    <path d="M0 60 C300 125 800 125 1200 38 L1200 120 L0 120Z" fill="#ffffff"/>
  </svg>
</section>

<div class="abs about-photo" role="img" aria-label="Black and white photo of a city waterfront under construction"></div>
<h2 class="abs section-title about-title">About Us</h2>
<p class="abs about-text">Located in Corvana Tech Park, a fully integrated technology park with the aim to foster technology and entrepreneurship, Brexalinth provides active operational support to medical device companies through the expertise of highly experienced and well-connected industry veterans. These veterans serve as mentors, interim-managers or as freelance consultants, enabling medical device companies to outsource key operational functions.</p>
<a class="abs btn about-btn">Learn More <span class="dot"></span></a>

<section class="abs services">
  <h2 class="abs section-title services-title">Our Serivces</h2>
  <span class="abs arrow" style="left:40px">&#8249;</span>
  <span class="abs arrow" style="right:40px">&#8250;</span>
  <div class="abs service-row">
    <div class="service"><div class="service-icon" role="img" aria-label="Money raising icon"><i></i></div><h3>Raise Capital</h3><p>Lorem ipsum dolor sit amet, consectetur adipiscing elit, sed do eiusmod</p></div>
    <div class="service"><div class="service-icon" role="img" aria-label="Growth chart icon"><i></i></div><h3>Assist and drive M&amp;A<br>strategies</h3><p>Lorem ipsum dolor sit amet, consectetur adipiscing</p></div>
    <div class="service"><div class="service-icon" role="img" aria-label="Target icon"><i></i></div><h3>Develop global sales and<br>marketing strategies</h3><p>Lorem ipsum dolor sit amet, consectetur adipiscing</p></div>
    <div class="service"><div class="service-icon" role="img" aria-label="Blueprint icon"><i></i></div><h3>Build and expand<br>distribution channels</h3><p>Lorem ipsum dolor sit amet, consectetur adipiscing</p></div>
  </div>
</section>

<h2 class="abs section-title located-title">Located in Dubai<br>Covering the World</h2>
<div class="abs map" role="img" aria-label="World map with connection lines from Dubai"></div>
<ul class="abs timeline">
  <li>The story of Dubai – from a small fishing village of palm frond huts to the most modern city in the world.</li>
  <li>In a matter of 25 years Dubai has shown the world what ambition, vision and leadership, coupled with determination to overcome the odds, can achieve.</li>
  <li>The story of Dubai symbolizes the ambition of many corporations and businesses around the globe.</li>
  <li>We are proud to call Dubai our home for the past 25 years, having witnessed the most dynamic phase of that growth.</li>
  <li>The Dubai story has inspired the founding of Brexalinth. A globally connected company, driven by passionate medical device industry experts, aiming for the exceptional and never the average.</li>
  <li>Connecting the global medical device world, helping young and established medical device companies to accelerate. Always with the goal to become the best – as impossible as it might seem.</li>
  <li>Dubai has shown the world – it is not impossible!</li>
</ul>

<svg class="footer-wave" width="1200" height="180" viewBox="0 0 1200 180">
  <path d="M0 120 C350 20 800 0 1200 70 L1200 180 L0 180Z" fill="var(--navy)"/>
  <path d="M0 140 C350 40 800 22 1200 90 L1200 180 L0 180Z" fill="var(--footer)"/>
</svg>
<footer class="abs footer">
  <div class="abs brand footer-brand">BREXALINTH</div>
  <div class="abs footer-col" style="left:112px"><h4>Quick Link</h4>Home<br>Who we are<br>Why use a prep 3PL<br>Benefits<br>Our software<br>Our Guarantee</div>
  <div class="abs footer-col" style="left:336px"><h4>Help Link</h4>Terms&amp;conditions<br>Privacy Policy<br>About Us<br>Support</div>
  <div class="abs newsletter-title">Join Our Newsletter</div>
  <div class="abs news-input">Enter Your Email</div>
  <div class="abs news-btn">Join Now</div>
  <div class="abs contact-line"><span>+ 000-000-0000</span><span>info@brexalinth.com</span><span class="socials"><span></span><span></span><span></span><span></span></span></div>
  <div class="abs faint-name" aria-hidden="true">BREXALINTH</div>
  <div class="abs footer-rule"></div>
  <div class="abs copyright">©Copyrights 2021 Brexalinth &nbsp;|&nbsp; All Rights Reserved</div>
</footer>

</body>
</html>
```